Webdesign für Physiotherapie
Sher angenehme Zusammenarbeit und hervoragendes Ergebniss - weiter so!
Zielgruppe
Physiotherapie unter ganzheitlichen oder umfangreicheren Gesichtspunkten.
ANLAGE BEACHTEN!
Aufgabenstellung
Siehe Anlage!

```html
<!DOCTYPE html>
<html lang="de">
<head>
<meta charset="utf-8">
<title>Florian Hallweg – Leistungen</title>
<link rel="stylesheet" href="https://fonts.googleapis.com/css2?family=Catamaran:wght@300;400;500;600&family=Dosis:wght@500;600;700&display=swap">
<style>
:root{
  --page:#f8f8f8;
  --panel:#f2f2f2;
  --red:#e23c22;
  --gold:#d4ad2c;
  --ink:#4a4a4a;
  --nav:#3a3a3a;
}
*{margin:0;padding:0;box-sizing:border-box}
html,body{width:1200px;height:3013px;overflow:hidden}
body{background:var(--page);font-family:"Catamaran",sans-serif;color:var(--ink);position:relative}
.brand{position:absolute;top:28px;left:0;width:1200px;text-align:center}
.brand-mark{width:84px;height:84px;border:5px solid var(--gold);border-radius:50%;margin:0 auto 8px}
.brand-name{font-family:"Dosis",sans-serif;font-weight:700;font-size:19px;color:var(--gold);letter-spacing:.5px}
.brand-sub{font-size:8px;color:var(--red);letter-spacing:1px;margin-top:2px}
.nav{position:absolute;top:170px;left:0;width:1200px;height:24px}
.nav a{position:absolute;transform:translateX(-50%);font-family:"Dosis",sans-serif;font-weight:700;font-size:17px;color:var(--nav);text-decoration:none;letter-spacing:.3px}
.nav a.active{color:var(--red)}
.hero{position:absolute;top:211px;left:0;width:1200px;height:348px;background:linear-gradient(90deg,#7fa9cf 0%,#cfc8c0 30%,#e8e2da 50%,#3f4a52 62%,#d8d2ca 80%,#b9b2a7 100%)}
.title{position:absolute;top:598px;left:0;width:1200px;text-align:center;font-weight:400;font-size:48px;color:var(--red)}
.intro{position:absolute;top:666px;left:222px;width:756px;text-align:center;font-size:11.5px;line-height:16px;font-weight:300;color:#555}
.card{position:absolute;left:67px;width:1066px;height:394px;display:flex}
.card .photo{width:533px;height:394px}
.card .text{width:533px;height:394px;background:var(--panel);padding:40px 40px 0 40px}
.card h2{font-weight:400;font-size:30px;color:var(--red);margin-bottom:8px;line-height:40px}
.card ul{list-style:none}
.card li{position:relative;padding-left:17px;font-size:15px;line-height:20px;margin-bottom:9px;font-weight:400}
.card li::before{content:"•";position:absolute;left:2px;top:0;font-size:12px;color:#666}
.closing{position:absolute;top:2562px;left:196px;width:808px;text-align:center;font-size:17px;line-height:23px;font-weight:600;color:#555}
.button{position:absolute;top:2644px;left:509px;width:182px;height:38px;border-radius:19px;background:var(--red);color:#fff;font-family:"Dosis",sans-serif;font-weight:700;font-size:18px;letter-spacing:1px;text-align:center;line-height:38px;text-decoration:none}
.stones{position:absolute;top:2702px;left:749px;width:345px;height:246px;border-radius:40% 40% 30% 30%;background:radial-gradient(ellipse at 55% 45%,#5a5a5a 0%,#2e2e2e 55%,rgba(248,248,248,0) 72%)}
.footer{position:absolute;top:2978px;left:0;width:1200px;height:35px;background:var(--gold);color:#fff;font-size:11.5px;font-weight:500}
.footer .copy{position:absolute;left:67px;top:10px}
.footer a{position:absolute;top:10px;color:#fff;text-decoration:underline}
</style>
</head>
<body>
<header class="brand">
  <div class="brand-mark"></div>
  <div class="brand-name">FLORIAN HALLWEG</div>
  <div class="brand-sub">Privatpraxis für Physiotherapie</div>
</header>
<nav class="nav">
  <a href="#" style="left:281px">START</a>
  <a href="#" class="active" style="left:444px">LEISTUNGEN</a>
  <a href="#" style="left:682px">BEHANDLUNGSMETHODEN</a>
  <a href="#" style="left:906px">KONTAKT</a>
</nav>
<div class="hero" role="img" aria-label="Foto: Therapeut mit Klemmbrett im Gespräch mit einer Patientin auf der Behandlungsliege"></div>

<h1 class="title">Leistungen</h1>
<p class="intro">Als leidenschaftlicher Physiotherapeut und sektoraler Heilpraktiker biete ich eine Vielzahl von professionellen Therapie- und Behandlungsdiensten an, um Ihre Gesundheit und Ihr Wohlbefinden zu verbessern. Mit meinem fundierten Fachwissen, meiner langjährigen Erfahrung und meiner Hingabe für meine Arbeit stehe ich Ihnen zur Seite, um individuelle Lösungen für Ihre spezifischen Bedürfnisse zu finden.</p>

<section class="card" style="top:752px">
  <div class="photo" role="img" aria-label="Foto: Behandlung des Nackens einer liegenden Patientin" style="background:linear-gradient(135deg,#8a5a3a 0%,#c9a98e 40%,#e9e4dc 60%,#7a7f80 100%)"></div>
  <div class="text">
    <h2>Physiotherapie</h2>
    <ul>
      <li>Manuelle Therapie: Gezielte Handgriffe zur Linderung von Schmerzen und zur Verbesserung der Beweglichkeit.</li>
      <li>Krankengymnastik: Maßgeschneiderte Übungen zur Rehabilitation und Stärkung der Muskulatur.</li>
      <li>Elektrotherapie: Einsatz von elektrischen Reizen zur Schmerzlinderung und Muskelstimulation.</li>
      <li>Kinesiotaping: Anwendung elastischer Tapes zur Unterstützung der Muskulatur und Gelenke.</li>
      <li>Lymphdrainage: Sanfte Massage zur Förderung des Lymphflusses und zur Entgiftung des Gewebes.</li>
    </ul>
  </div>
</section>

<section class="card" style="top:1199px">
  <div class="text">
    <h2>Holistische Therapien</h2>
    <ul>
      <li>Akupunktur: Stimulation bestimmter Punkte zur Harmonisierung des Energieflusses im Körper.</li>
      <li>Osteopathie: Ganzheitliche Behandlung zur Linderung von muskulären und strukturellen Dysfunktionen.</li>
      <li>Entspannungstechniken: Anleitung zu verschiedenen Entspannungsmethoden wie Atemübungen und Meditation.</li>
      <li>Naturheilkundliche Beratung: Unterstützung bei der Anwendung natürlicher Heilmittel und Lebensstiländerungen.</li>
    </ul>
  </div>
  <div class="photo" role="img" aria-label="Foto: Akupunkturnadeln werden in den Rücken gesetzt" style="background:linear-gradient(180deg,#8d9aa6 0%,#a6afb9 60%,#e2c6a6 78%,#d8b48f 100%)"></div>
</section>

<section class="card" style="top:1646px">
  <div class="photo" role="img" aria-label="Foto: Therapeut tastet die Schulter eines Patienten ab" style="background:linear-gradient(90deg,#c9b7a5 0%,#9fb5bf 35%,#a9bcc4 65%,#ddd9d4 100%)"></div>
  <div class="text">
    <h2>Präventive Maßnahmen</h2>
    <ul>
      <li>Ergonomische Beratung: Optimierung Ihrer Arbeits- und Lebensumgebung zur Vermeidung von Verletzungen.</li>
      <li>Rückenschule: Schulung in rückengerechtem Verhalten und Übungen zur Stärkung der Rückenmuskulatur.</li>
      <li>Gesundheitsvorträge: Informative Vorträge zu verschiedenen gesundheitsrelevanten Themen.</li>
      <li>Fitness- und Bewegungsprogramme: Individuell angepasste Übungsprogramme zur Förderung von Fitness und Wohlbefinden.</li>
    </ul>
  </div>
</section>

<section class="card" style="top:2092px">
  <div class="text">
    <h2>Beratung und Anleitung</h2>
    <ul>
      <li>Gesundheitsberatung: Individuelle Beratung zu einem gesunden Lebensstil und Präventionsmaßnahmen.</li>
      <li>Therapieplanung: Erstellung eines maßgeschneiderten Therapieplans zur Erreichung Ihrer Ziele.</li>
      <li>Selbsthilfeübungen: Anleitung zu Übungen und Techniken, die Sie zu Hause durchführen können.</li>
      <li>Hilfestellung bei der Auswahl geeigneter Hilfsmittel und Trainingsgeräte.</li>
    </ul>
  </div>
  <div class="photo" role="img" aria-label="Foto: Beratungsgespräch zwischen Therapeut und Patientin am Tisch" style="background:linear-gradient(135deg,#d9d4cc 0%,#c2a78a 45%,#e8e6e2 65%,#6f9ec4 100%)"></div>
</section>

<p class="closing">Mein Ziel ist es, Ihnen hochwertige und individuell angepasste Behandlungen anzubieten, um Ihre Gesundheit zu fördern, Schmerzen zu lindern und Ihre Lebensqualität zu verbessern. Kontaktieren Sie mich gerne, um einen Termin zu vereinbaren oder weitere Informationen zu meinen Leistungen zu erhalten.</p>
<a class="button" href="#">KONTAKT</a>

<div class="stones" role="img" aria-label="Foto: gestapelte schwarze Massagesteine mit Wassertropfen"></div>

<footer class="footer">
  <span class="copy">© 2023 Florian Hallweg</span>
  <a href="#" style="left:935px">Datenschutz</a>
  <a href="#" style="left:1061px">Impressum</a>
</footer>
</body>
</html>
```